Creative design for PLW Businesscard!

We would like a creative business card for our company The Maple Workshop. We situated in Barcelona and setup software development teams for companies in Belgium, Holland.

Orange is related to Holland.
PLW means cool in Dutch

* An Overview / Background of the Business & Services
o Setup and manage developer teams in Barcelona for for companies
in Holland, Belgium.
* The Target Market / Audience you are trying to reach
o Companies in Holland searching for developers
* Design Specifics; any preferences or ideas for Style, Colour,
Imagery, etc
o Orange, professional, fancy
o The Maple Workshop (PLW) means cool , good, nice

Target Market(s)

Companies in Holland searching for developers

Industry/Entity Type

Business

Contact Information for Business Card

Company name: The Maple Workshop

Name: Joost ter Haarveld

Title: Managing director (not necessary)

Email: joost@themapleworkshop.es

web: www.themapleworkshop.es

Phone: (+34) 932 487 113

Mobile: (+34) 668 302 947

Font styles to use
Other font styles liked:
• Bookman Old Style or Rockwell

Requirements
Must have
• Setup and manage developer teams in Barcelona for for companies
• in Holland, Belgium.

```html
<!DOCTYPE html>
<html lang="en">
<head>
<meta charset="utf-8">
<title>The Maple Workshop – Business Card</title>
<link href="https://fonts.googleapis.com/css2?family=Arvo:wght@400;700&display=swap" rel="stylesheet">
<style>
  :root {
    --page: #e9e4da;
    --paper: #ffffff;
    --ink: #2b2a2c;
    --dark-band: #333235;
    --orange: #f07424;
    --yellow: #f7c51c;
    --red: #ea3a46;
    --bevel: #d9d9d9;
    --muted: #6d6d70;
  }
  * { margin: 0; padding: 0; box-sizing: border-box; }
  html, body { width: 1200px; height: 1200px; overflow: hidden; }
  body {
    background: var(--page);
    font-family: "Arvo", serif;
    color: var(--ink);
    display: flex;
    flex-direction: column;
    align-items: center;
    justify-content: center;
    gap: 40px;
  }
  .card {
    position: relative;
    width: 880px;
    height: 520px;
    background: var(--paper);
    overflow: hidden;
    box-shadow: 0 6px 18px rgba(0,0,0,0.15);
  }
  .card-art { position: absolute; inset: 0; width: 100%; height: 100%; }
  .card-art--mirrored { transform: scaleX(-1); }

  /* Front */
  .company-name {
    position: absolute;
    left: 440px;
    top: 0;
    width: 420px;
    height: 520px;
    display: flex;
    align-items: center;
    justify-content: center;
    font-family: "Arvo", serif;
    font-size: 38px;
    font-weight: 400;
    color: var(--ink);
    white-space: nowrap;
  }

  /* Back */
  .contact-list {
    position: absolute;
    left: 56px;
    top: 150px;
    list-style: none;
    display: flex;
    flex-direction: column;
    gap: 18px;
    font-family: "Arvo", serif;
    font-size: 18px;
    color: var(--ink);
  }
  .contact-item { display: flex; align-items: center; gap: 14px; white-space: nowrap; }
  .contact-icon { width: 30px; height: 30px; flex: none; }
  .holder-name {
    position: absolute;
    left: 56px;
    top: 395px;
    font-family: "Arvo", serif;
    font-size: 36px;
    font-weight: 400;
    color: var(--ink);
    white-space: nowrap;
  }
  .holder-name-accent { color: var(--orange); }
</style>
</head>
<body>

<section class="card card--front" aria-label="Business card front">
  <svg class="card-art" viewBox="0 0 880 520" aria-hidden="true">
    <defs>
      <linearGradient id="front-stripe" x1="0" x2="1" y1="0" y2="0">
        <stop offset="0" stop-color="#f7c51c"/>
        <stop offset="0.55" stop-color="#f48a2a"/>
        <stop offset="1" stop-color="#ea3a46"/>
      </linearGradient>
    </defs>
    <rect x="0" y="0" width="460" height="165" fill="#333235"/>
    <rect x="0" y="345" width="460" height="175" fill="#333235"/>
    <rect x="120" y="222" width="300" height="72" fill="url(#front-stripe)"/>
    <circle cx="900" cy="260" r="585" fill="#d9d9d9"/>
    <circle cx="900" cy="260" r="572" fill="#ffffff"/>
    <circle cx="900" cy="260" r="536" fill="none" stroke="#f07424" stroke-width="7"/>
  </svg>
  <div class="company-name">The Maple Workshop</div>
</section>

<section class="card card--back" aria-label="Business card back">
  <svg class="card-art card-art--mirrored" viewBox="0 0 880 520" aria-hidden="true">
    <defs>
      <linearGradient id="back-stripe" x1="0" x2="1" y1="0" y2="0">
        <stop offset="0" stop-color="#f7c51c"/>
        <stop offset="0.55" stop-color="#f48a2a"/>
        <stop offset="1" stop-color="#ea3a46"/>
      </linearGradient>
    </defs>
    <rect x="0" y="0" width="460" height="165" fill="#333235"/>
    <rect x="0" y="345" width="460" height="175" fill="#333235"/>
    <rect x="120" y="222" width="300" height="72" fill="url(#back-stripe)"/>
    <circle cx="900" cy="260" r="585" fill="#d9d9d9"/>
    <circle cx="900" cy="260" r="572" fill="#ffffff"/>
    <circle cx="900" cy="260" r="536" fill="none" stroke="#f07424" stroke-width="7"/>
  </svg>

  <ul class="contact-list">
    <li class="contact-item">
      <svg class="contact-icon" viewBox="0 0 30 30" aria-label="Phone">
        <circle cx="15" cy="15" r="15" fill="#f07424"/>
        <rect x="11" y="7.5" width="8" height="15" rx="1.6" fill="none" stroke="#fff" stroke-width="1.6"/>
        <line x1="13.5" y1="19.5" x2="16.5" y2="19.5" stroke="#fff" stroke-width="1.4"/>
      </svg>
      <span>(+34) 932 487 113, (+34) 668 302 947</span>
    </li>
    <li class="contact-item">
      <svg class="contact-icon" viewBox="0 0 30 30" aria-label="Email">
        <circle cx="15" cy="15" r="15" fill="#6d6d70"/>
        <rect x="8" y="10" width="14" height="10" rx="1" fill="none" stroke="#fff" stroke-width="1.5"/>
        <polyline points="8.5,10.5 15,15.5 21.5,10.5" fill="none" stroke="#fff" stroke-width="1.5"/>
      </svg>
      <span>joost@themapleworkshop.es</span>
    </li>
    <li class="contact-item">
      <svg class="contact-icon" viewBox="0 0 30 30" aria-label="Website">
        <circle cx="15" cy="15" r="15" fill="#f07424"/>
        <circle cx="15" cy="15" r="7" fill="none" stroke="#fff" stroke-width="1.4"/>
        <ellipse cx="15" cy="15" rx="3" ry="7" fill="none" stroke="#fff" stroke-width="1.2"/>
        <line x1="8" y1="15" x2="22" y2="15" stroke="#fff" stroke-width="1.2"/>
      </svg>
      <span>www.themapleworkshop.es</span>
    </li>
  </ul>

  <h1 class="holder-name">Joost <span class="holder-name-accent">ter Haarveld</span></h1>
</section>

</body>
</html>
```